Redesign for existing homepage

We would like a redesign for our websites 2 column homepage
We provide engine repair and reconditioning services
We would like a cleaner, modern site that works well with our logo colors
Please see the attached brief for more info
Target Market(s)
25 - 45
Industry/Entity Type
Cleaner
Requirements
Must have
- Google Fonts

```html
<!DOCTYPE html>
<html lang="en">
<head>
<meta charset="utf-8">
<title>Wren Halloway Engine Reconditioners</title>
<link href="https://fonts.googleapis.com/css2?family=Open+Sans:ital,wght@0,300;0,400;0,600;1,300;1,400&display=swap" rel="stylesheet">
<style>
:root{
  --bg-yellow:#ffb900;
  --panel:#f4f4f4;
  --ink:#222;
  --muted:#8a8a8a;
  --accent-red:#e0201b;
  --nav-top:#3a3a3a;
  --nav-bottom:#050505;
  --nav-active:#ffb900;
  --footer:#1e1e1e;
  --line:#dcdcdc;
  --brand-blue:#1b3fd6;
}
*{box-sizing:border-box;margin:0;padding:0}
html,body{width:1026px;height:1200px;overflow:hidden}
body{background:var(--bg-yellow);font-family:"Open Sans",Arial,sans-serif;color:var(--ink);position:relative}
.page{position:absolute;left:130px;top:0;width:765px;height:1200px;background:var(--panel);box-shadow:0 0 14px rgba(0,0,0,.25)}
.abs{position:absolute}
.brand{left:24px;top:38px;display:flex;align-items:center;gap:10px}
.brand-dot{width:44px;height:44px;border-radius:50%;background:var(--brand-blue)}
.brand-name{font-size:22px;font-weight:600;color:var(--brand-blue);line-height:1.1}
.address{right:24px;top:63px;font-size:12.5px;font-weight:400}
.call{right:26px;top:84px;font-size:18px;font-weight:300}
.tagline{left:24px;top:128px;font-size:17.5px;font-weight:300}
.nav{left:24px;top:182px;width:718px;height:46px;display:flex;border-radius:3px;background:linear-gradient(var(--nav-top),var(--nav-bottom));overflow:hidden}
.nav a{display:flex;align-items:center;justify-content:center;color:#fff;text-decoration:none;font-size:11.3px;border-right:1px solid #555}
.nav a:last-child{border-right:none}
.nav a.active{color:var(--nav-active)}
.hero{left:24px;top:236px;width:718px;height:301px;background:linear-gradient(110deg,#d9d9d9 0%,#7a7a7a 45%,#3b3a38 70%,#5c564e 100%)}
.hero-side{left:24px;top:441px;width:352px;height:96px;background:linear-gradient(90deg,#1b4fb0,#2b64d0)}
.caption{left:24px;top:315px;width:353px;height:126px;background:rgba(240,240,240,.88);padding:12px 15px}
.caption h2{font-size:22px;font-weight:300;line-height:1.2;color:#333}
.caption p{font-size:10.4px;margin-top:10px;line-height:1.2;color:#111}
.dots{left:364px;top:506px;display:flex;gap:7px}
.dots span{width:12px;height:12px;border-radius:50%;background:#c8c8c8;border:1px solid #aaa}
.dots span.on{background:#fff}
.divider{left:467px;top:537px;width:1px;height:545px;background:var(--line);box-shadow:1px 0 3px rgba(0,0,0,.08)}
.h-section{font-size:19px;font-weight:300;color:#222}
.sub{font-size:13px;font-style:italic;font-weight:300;color:var(--accent-red)}
.para{font-size:10px;color:var(--muted);line-height:1.35}
.btn{display:flex;align-items:center;justify-content:center;color:#fff;font-size:10px;border-radius:3px;background:linear-gradient(#3a3a3a,#050505)}
.photo-oil{left:24px;top:817px;width:364px;height:145px;background:linear-gradient(100deg,#2b2b2b,#6a6a66 35%,#9a7a2a 48%,#3a3a3a 60%,#1a1a1a)}
.q{left:23px;font-size:10.8px;color:var(--muted);width:380px;line-height:1.3}
.field{background:#fff;border:1px solid #ddd;font-size:10px;color:#aaa;padding:0 10px;display:flex;align-items:center}
.field.area{align-items:flex-start;padding-top:10px}
.thumb{top:939px;width:81px;height:66px}
.feat-label{top:1009px;font-size:10px;color:var(--accent-red)}
.footer{left:0;top:1130px;width:765px;height:70px;background:var(--footer)}
.footer-links{left:24px;top:19px;display:flex;gap:12px;font-size:10.5px;color:#fff}
.copy{left:24px;top:41px;font-size:10px;color:#fff}
.social{left:622px;top:23px;display:flex;gap:1px}
.social span{width:26px;height:26px;border-radius:50%;background:#fff;border:2px solid #ddd}
</style>
</head>
<body>
<div class="page">
  <div class="abs brand"><span class="brand-dot"></span><span class="brand-name">Wren Halloway</span></div>
  <div class="abs address">Address: 212 Harbour Road, Eastbay, Wellington.</div>
  <div class="abs call">Call US : 04 555 0142</div>
  <div class="abs tagline">“Engine repairs and reconditioning specialists”</div>

  <nav class="abs nav">
    <a class="active" style="width:69px">Home</a>
    <a style="width:81px">About Us</a>
    <a style="width:183px">Private Vehicle Service &amp; Repair</a>
    <a style="width:120px">Trade Customers</a>
    <a style="width:163px">Race &amp; Classic Car Engines</a>
    <a style="width:102px">Contact Us</a>
  </nav>

  <div class="abs hero" role="img" aria-label="Mechanic in blue overalls working on a car's brake and suspension assembly"></div>
  <div class="abs hero-side" aria-hidden="true"></div>
  <div class="abs caption">
    <h2>Professional and knowledgeable workshop staff</h2>
    <p>We have an experienced and friendly team that are capable of providing you with a fantastic service.</p>
  </div>
  <div class="abs dots"><span class="on"></span><span></span><span></span></div>

  <div class="abs divider"></div>

  <h3 class="abs h-section" style="left:24px;top:578px">Welcome to Wren Halloway</h3>
  <div class="abs sub" style="left:24px;top:603px">Qualified, experienced and friendly engine reconditioning team</div>
  <p class="abs para" style="left:24px;top:637px;width:340px">Hi, my name is Wren Halloway and I own and manage Wren Halloway Engine Reconditioning Specialist Limited. WHER was started in 1982 and operated from our Eastbay workshop.</p>
  <div class="abs btn" style="left:24px;top:700px;width:68px;height:31px">Read More</div>

  <h3 class="abs h-section" style="left:23px;top:757px">Do You know ?</h3>
  <div class="abs sub" style="left:23px;top:781px">To have your car running at its best</div>
  <div class="abs photo-oil" role="img" aria-label="Motor oil being poured into an engine filler opening"></div>
  <p class="abs q" style="top:979px">Do you have a personal or family car that needs a repair?</p>
  <p class="abs q" style="top:1006px">Have a classic car that needs specialist engine work?</p>
  <p class="abs q" style="top:1032px">Own a race car that needs specialist engine repairs?</p>
  <p class="abs q" style="top:1058px;width:375px">Are you a garage owner, needing to outsource an engine machining job from one of your customers?</p>

  <h3 class="abs h-section" style="left:491px;top:584px">Get Free Quote</h3>
  <div class="abs field" style="left:493px;top:623px;width:172px;height:35px">Enter Your Name</div>
  <div class="abs field" style="left:493px;top:671px;width:172px;height:35px">Enter Your Name</div>
  <div class="abs field area" style="left:493px;top:719px;width:237px;height:109px">Enter Your Mesaage</div>
  <div class="abs btn" style="left:492px;top:845px;width:68px;height:32px">SUBMIT</div>

  <h3 class="abs h-section" style="left:489px;top:904px">Our Feature</h3>
  <div class="abs thumb" style="left:490px;background:linear-gradient(135deg,#1f3a6a,#5a6b80,#2a2a2a)" role="img" aria-label="Engine bay of a private vehicle"></div>
  <div class="abs thumb" style="left:574px;background:linear-gradient(135deg,#bdb8ae,#8a8f96,#3a3a3a)" role="img" aria-label="Mechanic inspecting a steaming engine"></div>
  <div class="abs thumb" style="left:659px;background:linear-gradient(135deg,#4a3a34,#2a2a2a,#7a2a22)" role="img" aria-label="Performance engine on a stand"></div>
  <div class="abs feat-label" style="left:491px">Private Vehicle?</div>
  <div class="abs feat-label" style="left:574px">Trade Customer?</div>
  <div class="abs feat-label" style="left:661px">Your passion?</div>
  <div class="abs btn" style="left:492px;top:1042px;width:83px;height:32px">Contact Now</div>

  <footer class="abs footer">
    <div class="abs footer-links"><span>Home</span><span>About Us</span><span>Private Vehicle Service &amp; Repair</span><span>Trade Customers</span><span>Race &amp; Classic Car Engines</span><span>Contact Us</span></div>
    <div class="abs copy">Copyright © 2014 whed.co. All rights reserved.</div>
    <div class="abs social" aria-label="Social links"><span></span><span></span><span></span><span></span></div>
  </footer>
</div>
</body>
</html>
```